Stationery design for law/Property/finance business

We need stationery design for a Law/Property/Finance business called Ridgemoor. Logo is attached.
we require a letterhead and with compliments slip.
Would like to see a very simple professional design using the colours of the logo and offset against Charcoal colours. Maybe a charcoal band for header and footer with logo and details appearing in it? Former letterhead attached for examples.
we require the project to be provided in word, pdf and jpeg format.
we require the following details on the stationery:
Cairns Phone: 07 40551926
Weipa Phone: 07 40613847
Mobile: 0491 570 384
Fax: 07 40338172
email: admin@ridgemoorholdings-example.com.au
ABN 51 824 306 917

```html
<!DOCTYPE html>
<html lang="en">
<head>
<meta charset="utf-8">
<title>Ridgemoor Stationery</title>
<link href="https://fonts.googleapis.com/css2?family=Open+Sans:ital,wght@0,400;0,600;1,400&family=Pinyon+Script&display=swap" rel="stylesheet">
<style>
  :root {
    --backdrop: #a9a8a9;
    --paper: #f5f4f2;
    --brand-blue: #2f7fc1;
    --flap-blue: #3377b4;
    --ink: #3f3f3f;
    --ink-soft: #555;
    --sign-tone: #d9d8d6;
  }
  * { box-sizing: border-box; margin: 0; padding: 0; }
  html, body { width: 1200px; height: 770px; overflow: hidden; }
  body {
    background: var(--backdrop);
    font-family: "Open Sans", Arial, sans-serif;
    color: var(--ink);
    position: relative;
  }
  .sheet {
    position: absolute;
    background: var(--paper);
    box-shadow: 2px 3px 6px rgba(0,0,0,.35);
  }
  .brand {
    position: absolute;
    display: flex;
    align-items: center;
    gap: 7px;
    color: var(--brand-blue);
    font-weight: 600;
    line-height: 1;
  }
  .brand-dot {
    width: 14px; height: 14px;
    border-radius: 50%;
    background: var(--brand-blue);
  }
  .icon { width: 8px; height: 8px; fill: var(--brand-blue); flex: none; }

  /* Letterhead */
  .letterhead { left: 61px; top: 33px; width: 497px; height: 701px; }
  .letterhead .brand { left: 37px; top: 72px; font-size: 26px; }
  .letterhead-contact {
    position: absolute; left: 325px; top: 25px;
    font-size: 8.4px; line-height: 12px; color: var(--ink-soft);
    list-style: none;
  }
  .letterhead-contact li { display: flex; align-items: center; gap: 5px; }
  .letterhead-contact .abn { padding-left: 0; }
  .letterhead-contact b { font-weight: 600; }
  .greeting {
    position: absolute; left: 36px; top: 196px;
    font-size: 13px; font-weight: 400; color: var(--ink-soft);
  }
  .letter-body {
    position: absolute; left: 36px; top: 237px; width: 425px;
    font-size: 7.3px; line-height: 12px; color: var(--ink-soft);
  }
  .letter-body p { margin-bottom: 12px; }
  .sign-off {
    position: absolute; left: 36px; top: 488px;
    font-size: 7.5px; color: var(--ink-soft);
  }
  .signature {
    position: absolute; left: 49px; top: 506px; width: 66px; height: 26px;
    background: var(--sign-tone);
  }
  .signatory {
    position: absolute; left: 54px; top: 542px;
    font-size: 8px; line-height: 13px; color: var(--ink-soft);
  }
  .letterhead-web {
    position: absolute; left: 0; right: 0; top: 678px;
    text-align: center; font-size: 8.5px; font-style: italic;
    letter-spacing: 1.4px; color: var(--ink-soft);
  }

  /* Envelope */
  .envelope-flap { position: absolute; left: 587px; top: 102px; width: 560px; height: 94px; }
  .envelope-flap-web {
    position: absolute; left: 0; width: 560px; top: 14px;
    text-align: center; font-size: 7.5px; color: #fff;
    transform: rotate(180deg);
  }
  .envelope { left: 587px; top: 195px; width: 560px; height: 255px; }
  .envelope .brand { left: 24px; top: 53px; font-size: 27px; }

  /* Compliments slip */
  .comp-slip { left: 587px; top: 477px; width: 560px; height: 253px; }
  .comp-slip .brand { left: 31px; top: 58px; font-size: 27px; }
  .comp-contact {
    position: absolute; left: 29px; top: 208px;
    font-size: 8.6px; line-height: 15px; color: var(--ink-soft);
  }
  .comp-contact .row { display: flex; align-items: center; gap: 3px; white-space: nowrap; }
  .comp-contact .row span { margin-right: 4px; }
  .comp-greeting {
    position: absolute; left: 357px; top: 186px;
    font-family: "Pinyon Script", cursive;
    font-size: 25px; color: var(--flap-blue);
    border-bottom: 1px solid var(--flap-blue);
    padding: 0 2px 0 2px; line-height: 30px; width: 172px;
  }
</style>
</head>
<body>

<svg width="0" height="0" style="position:absolute" aria-hidden="true">
  <defs>
    <symbol id="icon-phone" viewBox="0 0 16 16"><path d="M3.5 1l3 3-1.8 1.8a9 9 0 0 0 5.5 5.5L12 9.5l3 3-2 2.5C6.5 14.5 1.5 9.5 1 3z"/></symbol>
    <symbol id="icon-mobile" viewBox="0 0 16 16"><path d="M4 0h8a1 1 0 0 1 1 1v14a1 1 0 0 1-1 1H4a1 1 0 0 1-1-1V1a1 1 0 0 1 1-1zm1 2v10h6V2zm3 11a1 1 0 1 0 0 2 1 1 0 0 0 0-2z"/></symbol>
    <symbol id="icon-fax" viewBox="0 0 16 16"><path d="M4 0h8v5H4zM1 6h14v7h-2v3H3v-3H1zm4 5v3h6v-3z"/></symbol>
    <symbol id="icon-mail" viewBox="0 0 16 16"><path d="M0 3h16v1L8 9 0 4zm0 3l8 5 8-5v7H0z"/></symbol>
    <symbol id="icon-globe" viewBox="0 0 16 16"><path d="M8 0a8 8 0 1 0 0 16A8 8 0 0 0 8 0zm0 2c1 1.3 1.6 3.1 1.7 5H6.3C6.4 5.1 7 3.3 8 2zM2.1 9h2.3c.1 1.7.5 3.3 1.2 4.5A6 6 0 0 1 2.1 9zm0-2a6 6 0 0 1 3.5-4.5C4.9 3.7 4.5 5.3 4.4 7zm4.2 2h3.4c-.1 1.9-.7 3.7-1.7 5-1-1.3-1.6-3.1-1.7-5zm5.3 0h2.3a6 6 0 0 1-3.5 4.5c.7-1.2 1.1-2.8 1.2-4.5zm0-2c-.1-1.7-.5-3.3-1.2-4.5A6 6 0 0 1 13.9 7z"/></symbol>
  </defs>
</svg>

<!-- Letterhead -->
<section class="sheet letterhead">
  <div class="brand"><span class="brand-dot"></span>Ridgemoor</div>
  <ul class="letterhead-contact">
    <li class="abn">ABN 51 824 306 917</li>
    <li><svg class="icon"><use href="#icon-phone"/></svg>07 40551926 <b>(Cairns)</b></li>
    <li><svg class="icon"><use href="#icon-phone"/></svg>07 40613847 <b>(Weipa)</b></li>
    <li><svg class="icon"><use href="#icon-mobile"/></svg>0491 570 384</li>
    <li><svg class="icon"><use href="#icon-fax"/></svg>07 40338172</li>
    <li><svg class="icon"><use href="#icon-mail"/></svg>admin@ridgemoorholdings-example.com.au</li>
  </ul>

  <h1 class="greeting">Dear Mr. Harlow,</h1>
  <div class="letter-body">
    <p>Lorem ipsum dolor sit amet, consectetur adipiscing elit. Donec orci purus, luctus vitae dignissim eu, iaculis sed purus. Vivamus faucibus, ipsum nec aliquet viverra, leo mauris condimentum ligula, sit amet sagittis enim ligula quis arcu. Nam egestas tortor id nisi porttitor mattis. In tortor ante, ultricies in suscipit a, tempus non massa. Vivamus et auctor mi. Fusce vel massa nulla. Phasellus nec eros mauris, et scelerisque orci.</p>
    <p>Donec malesuada orci vitae nulla accumsan porta a id massa. Quisque accumsan iaculis magna sit amet fringilla. Maecenas consequat, magna eget tincidunt semper, odio nibh rutrum mi, id feugiat ante nisi eu risus. Vestibulum nunc orci, rhoncus a placerat in, ultricies in mi. Cras mattis varius eros, vel fringilla nisi suscipit eget. Quisque scelerisque sagittis nulla at porttitor.</p>
    <p>Sed id augue vitae urna euismod commodo aliquet a quam. Pellentesque arcu velit, cursus et malesuada ut, consequat et diam. Nullam erat sem, rhoncus id ullamcorper vitae, rhoncus et arcu. In ultricies ultricies nulla, ut rutrum nisi iaculis at. Donec eu magna a metus ornare faucibus. Fusce aliquet faucibus ultricies. Morbi semper, est id tincidunt gravida, sem arcu adipiscing lacus, ac bibendum nulla leo eu purus. Quisque nec diam sed risus consectetur accumsan quis quis nibh. Vestibulum id purus lorem.</p>
    <p>It is a long established fact that a reader will be distracted by the readable content of a page when looking at its layout. The point of using Lorem Ipsum is that it has a more-or-less normal distribution of letters, as opposed to using 'Content here, content here', making it look like readable English. Many desktop publishing packages</p>
  </div>
  <p class="sign-off">Sincerely,</p>
  <div class="signature" role="img" aria-label="Handwritten signature"></div>
  <p class="signatory">Peter Harlow<br>CEO/ Founder</p>
  <p class="letterhead-web">www.ridgemoorholdings-example.com.au</p>
</section>

<!-- Envelope -->
<div class="envelope-flap">
  <svg width="560" height="94" viewBox="0 0 560 94" aria-hidden="true">
    <path d="M0 94 L12 36 Q19 0 56 0 L504 0 Q541 0 548 36 L560 94 Z" fill="var(--flap-blue)"/>
  </svg>
  <p class="envelope-flap-web">ridgemoorholdings-example.com.au</p>
</div>
<section class="sheet envelope">
  <div class="brand"><span class="brand-dot"></span>Ridgemoor</div>
</section>

<!-- Compliments slip -->
<section class="sheet comp-slip">
  <div class="brand"><span class="brand-dot"></span>Ridgemoor</div>
  <div class="comp-contact">
    <div class="row">
      <svg class="icon"><use href="#icon-phone"/></svg><span>07 40551926 (Cairns)</span>
      <svg class="icon"><use href="#icon-phone"/></svg><span>07 40613847 (Weipa)</span>
      <svg class="icon"><use href="#icon-mobile"/></svg><span>0491 570 384</span>
    </div>
    <div class="row">
      <svg class="icon"><use href="#icon-fax"/></svg><span>07 40338172</span>
      <svg class="icon"><use href="#icon-mail"/></svg><span>admin@ridgemoorholdings-example.com.au</span>
      <svg class="icon"><use href="#icon-globe"/></svg><span>www.ridgemoorholdings-example.com.au</span>
    </div>
  </div>
  <p class="comp-greeting">With Compliments</p>
</section>

</body>
</html>
```